Sol Bocado Digital Menu Boards

IF SELECTED, WINNER MAY BE HIRED FOR OTHER DESIGNS OF DIFFERENT STORES OF OUR COMPANY.

Task: Digital Menu Boards Design

Task description: We need designs for a Digital Menu to be displayed on two 42’’screens at Solbocado, a fast-food restaurant in Guadalajara, Mexico. The menu redesign should communicate to our customers the experience of eating at our restaurant.

For avoiding the creation of videos, we are expecting several menu slides with the same text but with different images, simulating the effect of a video where the images are changing. This menu slides will be projected through a USB memory and a slideshow.

Attached files:
For the design, there are several documents attached to the task description:
1. Logo of the restaurant
2. Pictures of the restaurant
3. Example video of what we want to achieve through this menu slides.
4. Pictures of the actual menu board, to be replaced with the new designs.
5. Menu description (regular and breakfast menu)
6. Pictures of each element on the menu (We don’t have yet any breakfast pictures)
**The files are organized on a ZIP file.

Expected product:
For the regular menu,
• 2 menu slide designs for TACOS Y ESPECIALIDADES, where the text will be exactly the same but the images would differ.
• 2 menu slide designs for BEBIDAS Y EXTRAS, where the text will be exactly the same but the images would differ.
For the breakfast menu,
• 1 menu slide including all the menu
Total: 5 menu board slides.

Technical specs:
• You should send the editable file, med and high resolution JPGs for each design.
• The designs should fit perfectly on 42’’ screens.

Reason: Designers, For the final decision we are asking for a minimum of designs for chosing, we are going to wait a little bit more. Solbocado

Industry/Entity Type

Restaurant

```html
<!DOCTYPE html>
<html lang="es">
<head>
<meta charset="utf-8">
<title>Sol Bocado — Tacos y Especialidades</title>
<link href="https://fonts.googleapis.com/css2?family=Oswald:wght@400;700&family=Oranienbaum&display=swap" rel="stylesheet">
<style>
  :root {
    --bg-light: #ffffff;
    --bg-shade: #e4e4e6;
    --ink: #1f1f1f;
    --accent-red: #e8432a;
    --accent-salmon: #f4856a;
    --accent-green: #9ccf3a;
    --accent-blue: #2ec4e6;
    --badge-fill: #36c6e4;
    --badge-ring: #f3d51c;
    --brand-yellow: #f5cc1a;
    --white: #ffffff;
  }
  * { margin: 0; padding: 0; box-sizing: border-box; }
  html, body { width: 1200px; height: 600px; overflow: hidden; }
  body { background: var(--bg-light); }
  .menu-board {
    position: relative;
    width: 1200px;
    height: 600px;
    overflow: hidden;
    background: linear-gradient(100deg, var(--bg-light) 35%, var(--bg-shade) 100%);
  }
  .food-visual { position: absolute; left: 0; top: 0; }
  .dot { position: absolute; border-radius: 50%; }
  .dot--orange { left: 368px; top: 33px; width: 64px; height: 64px; background: var(--accent-red); }
  .dot--green { left: 490px; top: 406px; width: 52px; height: 52px; background: var(--accent-green); }
  .dot--salmon { left: 448px; top: 455px; width: 92px; height: 92px; background: var(--accent-salmon); }
  .dot--blue { left: 541px; top: 547px; width: 30px; height: 30px; background: var(--accent-blue); }

  .brand {
    position: absolute; left: 428px; top: 14px;
    width: 190px; height: 190px; border-radius: 50%;
    background: var(--brand-yellow);
    display: flex; align-items: center; justify-content: center;
  }
  .brand__name {
    font-family: "Oswald", sans-serif; font-weight: 700;
    font-size: 34px; color: var(--accent-red); line-height: 1;
  }

  .board-title {
    position: absolute; left: 640px; top: 28px;
    font-family: "Oswald", sans-serif; font-weight: 700;
    font-size: 40px; letter-spacing: 1px; color: var(--ink); line-height: 1.1;
  }
  .board-title__rule {
    position: absolute; left: 632px; top: 84px; width: 568px; height: 4px;
    background: var(--accent-red);
  }

  .col-head {
    position: absolute; width: 140px; text-align: center;
    font-family: "Oswald", sans-serif; font-weight: 400;
    font-size: 19px; line-height: 1.05; color: var(--ink);
    transform: translateX(-50%) scaleX(0.85);
  }
  .col-head--pastor { left: 815px; top: 133px; }
  .col-head--arrachera { left: 960px; top: 133px; }
  .col-head--harina { left: 1108px; top: 133px; }

  .item-name {
    position: absolute; right: 442px;
    font-family: "Oranienbaum", serif; font-size: 60px;
    color: var(--ink); line-height: 1; transform-origin: right center;
    transform: scaleX(0.88);
  }
  .price {
    position: absolute; width: 94px; height: 94px; border-radius: 50%;
    background: var(--badge-fill); border: 7px solid var(--badge-ring);
    display: flex; align-items: center; justify-content: center;
    font-family: "Oswald", sans-serif; font-weight: 700; font-size: 36px;
    color: var(--white); transform: translate(-50%, -50%);
  }
</style>
</head>
<body>
<main class="menu-board">
  <svg class="food-visual" width="600" height="600" viewBox="0 0 600 600" role="img" aria-label="Photo of fresh guacamole with diced tomato and a lime wedge in a white bowl">
    <defs>
      <linearGradient id="guacamoleTone" x1="0" y1="0" x2="1" y2="1">
        <stop offset="0" stop-color="#e9f07a"/>
        <stop offset="0.35" stop-color="#b9d25a"/>
        <stop offset="0.75" stop-color="#8fb544"/>
        <stop offset="1" stop-color="#dfe6d4"/>
      </linearGradient>
    </defs>
    <path d="M0 0 H414 A400 400 0 0 1 470 600 H0 Z" fill="url(#guacamoleTone)"/>
  </svg>

  <span class="dot dot--orange"></span>
  <span class="dot dot--green"></span>
  <span class="dot dot--salmon"></span>
  <span class="dot dot--blue"></span>

  <div class="brand"><span class="brand__name">Sol Bocado</span></div>

  <h1 class="board-title">TACOS Y ESPECIALIDADES</h1>
  <div class="board-title__rule"></div>

  <div class="col-head col-head--pastor">Pastor</div>
  <div class="col-head col-head--arrachera">Arrachera</div>
  <div class="col-head col-head--harina">Tortilla de<br>Harina</div>

  <div class="item-name" style="top:218px">Tacos:</div>
  <div class="item-name" style="top:310px">Quesadilla:</div>
  <div class="item-name" style="top:405px">Gringa:</div>
  <div class="item-name" style="top:502px">Volcán:</div>

  <div class="price" style="left:815px;top:244px">$14</div>
  <div class="price" style="left:960px;top:244px">$16</div>
  <div class="price" style="left:1108px;top:244px">+ $1</div>

  <div class="price" style="left:815px;top:337px">$18</div>
  <div class="price" style="left:960px;top:337px">$20</div>
  <div class="price" style="left:1108px;top:337px">+ $1</div>

  <div class="price" style="left:815px;top:433px">$20</div>
  <div class="price" style="left:960px;top:433px">$16</div>
  <div class="price" style="left:1108px;top:433px">+ $2</div>

  <div class="price" style="left:815px;top:530px">$18</div>
  <div class="price" style="left:960px;top:530px">$20</div>
  <div class="price" style="left:1108px;top:530px">+ $1</div>
</main>
</body>
</html>
```